New business logo / Business Card Design

My company provides Interim Management and consultancy, for Facilities Services. Covers any aspect of facilities management, including M&E, helpdesk, asset management, supplier relationships, catering, cleaning etc. Company provides innovative solutions to exceed client needs, drawing on years of experience. Initial thoughts on logo are attached below. Fits with RAG status on projects, red, amber and green, with logo design colours around moving services from amber to green.

Target Market(s)

Facilities Management clients and service providers

Industry/Entity Type

Business

Contact Information for Business Card

Company Name = k7Rventures Ltd My name on card = Derek Whitcombe, Director Mobile = 07516309842 Email = Derek@k7rventuresltd.co.uk Twitter = @k7Rventures Ltd

Font styles to use
Sans Serif

Colors
f37122
00a990

Requirements
Must have
• Logo to be evident, with some background image in reference to Facilities Management

```html
<!DOCTYPE html>
<html lang="en">
<head>
<meta charset="utf-8">
<title>k7Rventures Ltd – Business Card</title>
<link href="https://fonts.googleapis.com/css2?family=Mulish:wght@400;700;800&display=swap" rel="stylesheet">
<style>
  :root {
    --backdrop: #1c1c1c;
    --card-white: #f7f7f5;
    --card-dark: #454545;
    --text-dark: #4a4a4a;
    --text-light: #ececec;
    --accent-green: #8cb23a;
  }
  * { margin: 0; padding: 0; box-sizing: border-box; }
  html, body {
    width: 1200px; height: 1001px; overflow: hidden;
    background: var(--backdrop);
    font-family: "Mulish", sans-serif;
  }
  .card {
    position: absolute; left: 345px;
    width: 510px; height: 337px;
    overflow: hidden;
  }
  .card--front { top: 135px; background: var(--card-white); }
  .card--back { top: 529px; background: var(--card-dark); }
  .card__divider { position: absolute; inset: 0; }
  .brand-name {
    position: absolute;
    font-weight: 800; font-size: 34px; letter-spacing: -0.5px;
    line-height: 1; white-space: nowrap;
  }
  .card--front .brand-name { left: 38px; top: 62px; color: var(--text-dark); }
  .card--back .brand-name { left: 0; right: 0; top: 146px; text-align: center; color: var(--text-light); }
  .person { position: absolute; left: 37px; top: 146px; color: var(--text-dark); }
  .person__name { font-weight: 700; font-size: 17px; letter-spacing: 0.3px; text-transform: uppercase; }
  .person__role { font-size: 13px; margin-top: 1px; }
  .contacts {
    position: absolute; right: 39px; top: 226px;
    list-style: none; color: var(--text-light);
    font-size: 12.5px; line-height: 17px;
  }
  .contacts li { display: flex; justify-content: flex-end; align-items: center; gap: 9px; }
  .contacts svg { width: 13px; height: 13px; flex: none; }
  .back-url {
    position: absolute; left: 0; right: 0; top: 264px;
    text-align: center; color: var(--text-light); font-size: 12.5px;
  }
</style>
</head>
<body>
  <section class="card card--front">
    <svg class="card__divider" viewBox="0 0 510 337" aria-hidden="true">
      <path fill="var(--card-dark)" d="M0,240 C160,270 300,150 510,150 L510,337 L0,337 Z"/>
    </svg>
    <div class="brand-name">k7Rventures Ltd</div>
    <div class="person">
      <div class="person__name">Derek Whitcombe</div>
      <div class="person__role">Director</div>
    </div>
    <ul class="contacts">
      <li>07516309842
        <svg viewBox="0 0 13 13"><rect width="13" height="13" rx="2.5" fill="var(--accent-green)"/><rect x="4" y="2.5" width="5" height="8" rx="1" fill="none" stroke="var(--card-dark)" stroke-width="1.2"/></svg></li>
      <li>@k7Rventures Ltd
        <svg viewBox="0 0 13 13"><rect width="13" height="13" rx="2.5" fill="var(--accent-green)"/></svg></li>
      <li>Derek@k7rventuresltd.co.uk
        <svg viewBox="0 0 13 13"><rect width="13" height="13" rx="2.5" fill="var(--accent-green)"/><rect x="2.5" y="3.5" width="8" height="6" fill="none" stroke="var(--card-dark)" stroke-width="1.1"/><path d="M2.5,3.5 L6.5,7 L10.5,3.5" fill="none" stroke="var(--card-dark)" stroke-width="1.1"/></svg></li>
      <li>www.k7rventuresltd.co.uk
        <svg viewBox="0 0 13 13"><rect width="13" height="13" rx="2.5" fill="var(--accent-green)"/><circle cx="6.5" cy="6.5" r="4" fill="none" stroke="var(--card-dark)" stroke-width="1"/><path d="M2.5,6.5 H10.5" stroke="var(--card-dark)" stroke-width="0.9"/></svg></li>
    </ul>
  </section>

  <section class="card card--back">
    <div class="brand-name">k7Rventures Ltd</div>
    <div class="back-url">www.k7rventuresltd.co.uk</div>
  </section>
</body>
</html>
```